Please design a business card with my current logo (attached below).

I have some specifics that must be included:
1. I want the emphasis on Licensed Heritage Home Transfer Consultant.
2. Leave room for my picture.
3. Company name, address, phone numbers and email address.
4. My BRE# should be placed under my name.

```html
<!DOCTYPE html>
<html lang="en">
<head>
<meta charset="utf-8">
<title>Maren Holt — Business Card</title>
<link rel="stylesheet" href="https://fonts.googleapis.com/css2?family=Cinzel:wght@400;700&family=Tinos:wght@400;700&display=swap">
<style>
  :root {
    --backdrop: #e6e7e9;
    --paper: #ffffff;
    --charcoal: #262729;
    --charcoal-deep: #18191b;
    --brand-red: #c4161c;
    --band-text: #3a0a0b;
    --ink-light: #f2f2f2;
    --ink-dark: #2b2b2b;
  }
  * { box-sizing: border-box; margin: 0; padding: 0; }
  html, body {
    width: 1200px; height: 900px; overflow: hidden;
    background: var(--backdrop);
  }
  .stage {
    position: relative; width: 1200px; height: 900px;
  }
  .card {
    position: absolute; top: 300px;
    width: 525px; height: 300px;
    border-radius: 24px; overflow: hidden;
    box-shadow: 0 10px 24px rgba(0,0,0,0.18);
  }
  .card--front { left: 50px; background: var(--paper); }
  .card--back {
    left: 625px;
    background: linear-gradient(160deg, #34363a 0%, var(--charcoal) 45%, var(--charcoal-deep) 100%);
  }

  /* front */
  .front-top { position: absolute; left: 0; top: 0; width: 100%; height: 136px; background: var(--paper); }
  .brand {
    position: absolute; left: 22px; top: 40px;
    display: flex; flex-direction: column; align-items: flex-start; gap: 10px;
  }
  .brand__mark { width: 22px; height: 22px; background: var(--charcoal); margin-left: 62px; }
  .brand__name {
    font-family: "Cinzel", serif; font-weight: 400;
    font-size: 30px; letter-spacing: 0.5px; color: var(--ink-dark);
  }
  .portrait {
    position: absolute; right: 0; top: 0; width: 200px; height: 148px;
    background: linear-gradient(180deg, #ffffff 0%, #f1ece8 35%, #3a3b3f 100%);
  }
  .tagline-band {
    position: absolute; left: 0; top: 136px; width: 100%; height: 16px;
    background: var(--brand-red);
    font-family: "Tinos", serif; font-size: 11.5px; letter-spacing: 2.6px;
    color: var(--band-text); line-height: 16px; padding-left: 16px; white-space: nowrap;
  }
  .front-bottom {
    position: absolute; left: 0; top: 152px; width: 100%; height: 148px;
    background: linear-gradient(180deg, #2d2e31 0%, var(--charcoal-deep) 100%);
  }
  .agent { position: absolute; left: 18px; top: 6px; font-family: "Tinos", serif; }
  .agent__name { color: var(--brand-red); font-size: 17px; line-height: 20px; }
  .agent__license { color: var(--ink-light); font-size: 11px; line-height: 14px; }
  .contact {
    position: absolute; left: 18px; top: 50px; list-style: none;
    font-family: "Tinos", serif; font-size: 13px; color: var(--ink-light);
  }
  .contact li { display: flex; align-items: center; gap: 6px; height: 18px; }
  .contact svg { width: 11px; height: 11px; fill: var(--brand-red); flex: none; }

  /* back */
  .back-brand {
    position: absolute; inset: 0;
    display: flex; flex-direction: column; align-items: center; justify-content: center; gap: 22px;
  }
  .back-brand__mark { width: 54px; height: 54px; background: var(--brand-red); }
  .back-brand__name {
    font-family: "Cinzel", serif; font-weight: 400;
    font-size: 48px; letter-spacing: 1px; color: var(--ink-light);
  }
</style>
</head>
<body>
<main class="stage">

  <section class="card card--front" aria-label="Business card front">
    <div class="front-top">
      <div class="brand">
        <span class="brand__mark"></span>
        <span class="brand__name">Maren Holt</span>
      </div>
    </div>
    <div class="portrait" role="img" aria-label="Portrait photo of the agent in a dark suit, arms folded"></div>
    <div class="tagline-band">Licensed Heritage Home Transfer Consultant.</div>
    <div class="front-bottom">
      <div class="agent">
        <p class="agent__name">Maren Holt</p>
        <p class="agent__license">BRE#10294736</p>
      </div>
      <ul class="contact">
        <li>
          <svg viewBox="0 0 24 24" aria-hidden="true"><path d="M6.6 10.8a15.1 15.1 0 0 0 6.6 6.6l2.2-2.2a1 1 0 0 1 1-.25 11.4 11.4 0 0 0 3.6.57 1 1 0 0 1 1 1V20a1 1 0 0 1-1 1A17 17 0 0 1 3 4a1 1 0 0 1 1-1h3.5a1 1 0 0 1 1 1c0 1.25.2 2.45.57 3.57a1 1 0 0 1-.25 1z"/></svg>
          (916) 555-0148
        </li>
        <li>
          <svg viewBox="0 0 24 24" aria-hidden="true"><path d="M2 5h20v14H2z M4 7v.5l8 5 8-5V7l-8 5z" fill-rule="evenodd"/></svg>
          maren.holt@mailbox.com
        </li>
        <li>
          <svg viewBox="0 0 24 24" aria-hidden="true"><path d="M12 2a10 10 0 1 0 0 20 10 10 0 0 0 0-20zm0 2c.9 1.2 1.6 2.6 2 4h-4c.4-1.4 1.1-2.8 2-4zM4.3 14a8 8 0 0 1 0-4h3.4a16 16 0 0 0 0 4zm.9 2h2.9c.4 1.3.9 2.5 1.6 3.6A8 8 0 0 1 5.2 16zM8.1 8H5.2a8 8 0 0 1 4.5-3.6C9 5.5 8.5 6.7 8.1 8zM12 20c-.9-1.2-1.6-2.6-2-4h4c-.4 1.4-1.1 2.8-2 4zm2.3-6H9.7a14 14 0 0 1 0-4h4.6a14 14 0 0 1 0 4zm.3 5.6c.7-1.1 1.2-2.3 1.6-3.6h2.9a8 8 0 0 1-4.5 3.6zm1.7-5.6a16 16 0 0 0 0-4h3.4a8 8 0 0 1 0 4z"/></svg>
          www.marenholt.com
        </li>
        <li>
          <svg viewBox="0 0 24 24" aria-hidden="true"><path d="M12 3 2 12h3v8h5v-5h4v5h5v-8h3z"/></svg>
          4172 Willow Creek Road, Suite D,
        </li>
      </ul>
    </div>
  </section>

  <section class="card card--back" aria-label="Business card back">
    <div class="back-brand">
      <span class="back-brand__mark"></span>
      <span class="back-brand__name">Maren Holt</span>
    </div>
  </section>

</main>
</body>
</html>
```